The Brightwater Compass Business Card

We need an attractive business card with the logo that we bought from ArtVantly last year.
Our mission is to contribute to change the way today's leaders manage business companies bringing value to the workplace and helping them to build a new model of creating wealth.
Our logo is clear about our values : we seek Positive Change through People and are convinced that the pursuit of individual well-being and the chase of economic results can converge with the right management.
Management Consulting
Corinne Fabrelle
+34 612 98 70 31
corinne.fabrelle@thebrightwatercompass-mail.net
www.thebrightwatercompass-mail.net

```html
<!DOCTYPE html>
<html lang="en">
<head>
<meta charset="utf-8">
<title>The Brightwater Compass Business Card</title>
<link rel="stylesheet" href="https://fonts.googleapis.com/css2?family=Cinzel:wght@400;700&family=Hind:wght@400&display=swap">
<style>
  :root {
    --backdrop: #808080;
    --card: #ffffff;
    --card-tint: #f6f7f7;
    --leaf-tone: #e9eded;
    --teal: #1b8781;
    --ink: #1d2747;
    --rule: #b9c4c3;
  }
  * { margin: 0; padding: 0; box-sizing: border-box; }
  html, body {
    width: 1200px;
    height: 900px;
    overflow: hidden;
    background: var(--backdrop);
  }
  .canvas {
    position: relative;
    width: 1200px;
    height: 900px;
  }
  .card {
    position: absolute;
    top: 271px;
    width: 457px;
    height: 281px;
    border-radius: 14px;
    background: var(--card);
    overflow: hidden;
    text-align: center;
  }
  .card--front { left: 137px; }
  .card--back { left: 626px; }
  .leaf-backdrop {
    position: absolute;
    inset: 0;
    background: linear-gradient(135deg, var(--card-tint) 0%, var(--leaf-tone) 50%, var(--card-tint) 100%);
    opacity: 0.8;
  }
  .brand {
    position: absolute;
    left: 0;
    right: 0;
    display: flex;
    flex-direction: column;
    align-items: center;
  }
  .brand-dot {
    border-radius: 50%;
    background: var(--teal);
  }
  .brand-name {
    font-family: "Cinzel", serif;
    font-weight: 400;
    color: var(--teal);
    white-space: nowrap;
    line-height: 1;
  }
  .card--front .brand { top: 36px; }
  .card--front .brand-dot { width: 36px; height: 36px; margin-bottom: 24px; }
  .card--front .brand-name { font-size: 22px; }
  .card--back .brand { top: 94px; }
  .card--back .brand-dot { width: 46px; height: 46px; margin-bottom: 30px; }
  .card--back .brand-name { font-size: 26px; }
  .holder {
    position: absolute;
    top: 161px;
    left: 0;
    right: 0;
    font-family: "Cinzel", serif;
    font-weight: 700;
    font-size: 17px;
    color: var(--teal);
    letter-spacing: 0.3px;
    line-height: 1;
  }
  .holder-rule {
    position: absolute;
    top: 189px;
    left: 168px;
    width: 122px;
    height: 1px;
    background: var(--rule);
  }
  .contact {
    position: absolute;
    top: 198px;
    left: 0;
    right: 0;
    list-style: none;
    font-family: "Hind", sans-serif;
    font-size: 13px;
    line-height: 19px;
    color: var(--ink);
  }
</style>
</head>
<body>
<main class="canvas">
  <section class="card card--front">
    <div class="leaf-backdrop" role="img" aria-label="Soft pattern of pale scattered leaves across the card"></div>
    <div class="brand">
      <span class="brand-dot"></span>
      <span class="brand-name">The Brightwater Compass</span>
    </div>
    <h1 class="holder">CORINNE FABRELLE</h1>
    <div class="holder-rule"></div>
    <ul class="contact">
      <li>+34 612 98 70 31</li>
      <li>corinne.fabrelle@thebrightwatercompass-mail.net</li>
      <li>www.thebrightwatercompass-mail.net</li>
    </ul>
  </section>
  <section class="card card--back">
    <div class="brand">
      <span class="brand-dot"></span>
      <span class="brand-name">The Brightwater Compass</span>
    </div>
  </section>
</main>
</body>
</html>
```